Flyer Ballettschule
Vielen Dank für den wirklich sehr professionellen superschönen Flyer. Uns hat das Design beim ersten Entwurf schon perfekt gefallen. Sofort hat der Designer kleine Änderungen bestens umgesetzt. Sehr netter Kontakt. Ein ganz großes Dankeschön! Ballettschule Wendelmoor

```html
<!DOCTYPE html>
<html lang="de">
<head>
<meta charset="utf-8">
<title>Flyer Ballettschule Wendelmoor</title>
<link href="https://fonts.googleapis.com/css2?family=Crimson+Text:ital,wght@0,400;0,600;0,700;1,400&family=Great+Vibes&display=swap" rel="stylesheet">
<style>
  :root{
    --red:#dc1f26;
    --ink:#4a4a4c;
    --band:#58585a;
    --paper:#ffffff;
    --mist:#ececec;
    --mist-light:#f4f4f4;
    --canvas:#eeeeec;
  }
  *{margin:0;padding:0;box-sizing:border-box}
  html,body{width:1200px;height:990px;overflow:hidden;background:var(--canvas)}
  body{position:relative;font-family:"Crimson Text",Georgia,serif;color:var(--ink)}
  .flyer{position:absolute;top:43px;width:422px;height:905px;background:var(--paper);overflow:hidden}
  .flyer--front{left:147px}
  .flyer--back{left:652px}
  .abs{position:absolute}
  ul{list-style:none}

  /* front */
  .hero-photo{left:0;top:0;width:422px;height:188px;background:linear-gradient(120deg,#eaeaea 0%,#f6f6f6 45%,#e2e2e2 100%)}
  .brand-name{left:40px;top:112px;font-weight:600;font-size:25px;line-height:28px;color:var(--red)}
  .brand-name span{display:block}
  .brand-name span+span{padding-left:42px}
  .invite-band{left:0;top:188px;width:422px;height:98px;background:var(--band)}
  .invite-band h1{position:absolute;left:24px;top:24px;font-weight:600;font-size:21px;line-height:28px;color:#fff;letter-spacing:.4px}
  .ribbon{left:330px;top:178px;width:88px;height:128px}
  .ribbon-text{left:330px;top:183px;width:80px;text-align:center;color:#fff}
  .ribbon-text .years{font-style:italic;font-size:50px;line-height:48px}
  .ribbon-text .word{font-family:"Great Vibes",cursive;font-size:30px;line-height:28px}
  .ribbon-text .place{font-family:"Great Vibes",cursive;font-size:14px;line-height:18px}

  .section{position:absolute;left:0;width:422px}
  .section--youth{top:286px;height:247px;background:var(--mist)}
  .section--adults{top:533px;height:189px;background:var(--mist-light)}
  .section--contact{top:722px;height:138px;background:var(--mist-light)}
  .section-title{position:absolute;left:24px;font-weight:700;font-size:15px;color:var(--red);letter-spacing:.3px;text-transform:uppercase}
  .course-list{position:absolute;left:24px}
  .course-list li{position:relative;padding-left:27px;font-weight:600;font-size:15px;color:var(--ink)}
  .course-list li::before,.benefit-list li::before{content:"∾";position:absolute;left:0;top:0;font-weight:400;color:#555}
  .section--youth .section-title{top:15px}
  .section--youth .course-list{top:37px}
  .section--youth .course-list li{line-height:23px}
  .section--adults .section-title{top:14px}
  .section--adults .course-list{top:34px}
  .section--adults .course-list li{line-height:21px}
  .course-list small{display:block;font-size:11px;line-height:14px;font-weight:600}
  .section--contact .section-title{top:7px}
  .contact{position:absolute;left:24px;top:27px;font-size:13px;line-height:17px;color:#555}
  .dancer-figure{left:282px;top:490px;width:140px;height:370px;background:radial-gradient(ellipse at 45% 45%,rgba(220,31,38,.55) 0%,rgba(220,31,38,.25) 55%,rgba(220,31,38,0) 80%)}
  .site-band{left:0;top:860px;width:422px;height:45px;background:var(--band);color:#fff;text-align:center;font-weight:600;font-size:17px;line-height:45px;letter-spacing:.8px}

  /* back */
  .quote-photo{left:0;top:0;width:422px;height:293px;background:linear-gradient(180deg,#dedede 0%,#e9e9e9 60%,#ffffff 100%)}
  .shoe-photo{left:242px;top:0;width:162px;height:257px;background:linear-gradient(160deg,#e8b89d 0%,#f0c9b2 45%,#9a9a9a 100%);border-radius:0 0 40px 40px;opacity:.85}
  .quote{left:14px;top:18px;font-size:31px;line-height:29px}
  .quote span{display:block}
  .quote .soft{color:#5a5a5c;font-weight:400}
  .quote .strong{color:var(--red);font-weight:700}
  .quote .i1{padding-left:0}
  .quote .i2{padding-left:60px}
  .quote .i3{padding-left:7px}
  .quote .i4{padding-left:86px}
  .copy{left:21px;top:302px;width:385px;font-size:14px;line-height:18px}
  .copy .lead-title{font-weight:700;color:var(--red);text-transform:uppercase;font-size:14.5px}
  .copy .lead{font-weight:700;color:var(--ink)}
  .copy p{margin-bottom:18px}
  .benefit-intro{margin-bottom:5px!important}
  .benefit-list{margin-bottom:18px}
  .benefit-list li{position:relative;padding-left:27px;line-height:18.2px}
  .copy .bold{font-weight:700}
  .copy .accent{font-weight:700;color:var(--red)}
  .gallery-photo{top:715px;height:129px}
  .gallery-photo--show{left:0;width:208px;background:linear-gradient(135deg,#9c5a4a 0%,#e7c9d6 50%,#d8607e 100%)}
  .gallery-photo--class{left:213px;width:209px;background:linear-gradient(135deg,#c2252c 0%,#2a2f45 55%,#8a6a4e 100%)}
  .membership{left:0;top:866px;width:422px;text-align:center;font-weight:700;font-size:16px;color:var(--red);letter-spacing:.6px;text-transform:uppercase}
</style>
</head>
<body>

<section class="flyer flyer--front">
  <div class="hero-photo abs" role="img" aria-label="Foto: Tänzerinnen in weißen Strumpfhosen und Ballettschuhen an der Stange"></div>
  <div class="brand-name abs"><span>Ballettschule</span><span>Wendelmoor</span></div>

  <div class="invite-band abs">
    <h1>HERZLICHE EINLADUNG<br>ZU EINER PROBESTUNDE</h1>
  </div>
  <svg class="ribbon abs" viewBox="0 0 88 128" aria-hidden="true">
    <polygon points="80,0 88,8 80,8" fill="#9e1419"/>
    <polygon points="0,0 80,0 80,126 40,110 0,126" fill="var(--red)"/>
  </svg>
  <div class="ribbon-text abs">
    <div class="years">40</div>
    <div class="word">Jahre</div>
    <div class="place">in Wiesental</div>
  </div>

  <div class="section section--youth">
    <h2 class="section-title">Kinder und Jugendliche</h2>
    <ul class="course-list">
      <li>Tänzerische Früherziehung ab 3 Jahren</li>
      <li>Ballettvorbereitung ab 4 Jahren</li>
      <li>Klassisches Ballett ab 6 Jahren</li>
      <li>Klassisches Ballett mit Spitze ab 12 Jahren</li>
      <li>Jazz Tanz</li>
      <li>Step Tanz</li>
      <li>Hip Hop</li>
      <li>Berufsvorbereitung Tanz</li>
    </ul>
  </div>

  <div class="section section--adults">
    <h2 class="section-title">Erwachsene</h2>
    <ul class="course-list">
      <li>Klassisches Ballett<small>(auch für Anfänger und Wiedereinsteiger)</small></li>
      <li>Jazz Tanz</li>
      <li>Step Tanz</li>
      <li>Flamenco</li>
      <li>Tänzerische Gymnastik 50+, 70+</li>
    </ul>
  </div>

  <div class="section section--contact">
    <h2 class="section-title">Ballettschule Wendelmoor</h2>
    <address class="contact" style="font-style:normal">
      Inh. Marlene Wendelmoor<br>
      Lindenhofer Straße 14<br>
      25498 Wiesental-Mitte<br>
      Telefon: 0 41 07 - 52 63 190<br>
      Mobil: 0 176 - 38 27 604<br>
      info@ballettschule-wendelmoor.de
    </address>
  </div>

  <div class="dancer-figure abs" role="img" aria-label="Rote Silhouette einer Ballerina in Arabesque"></div>

  <div class="site-band abs">WWW.BALLETTSCHULE-WENDELMOOR.DE</div>
</section>

<section class="flyer flyer--back">
  <div class="quote-photo abs" role="img" aria-label="Hintergrund mit hellgrauem Damastmuster"></div>
  <div class="shoe-photo abs" role="img" aria-label="Foto: roséfarbene Spitzenschuhe auf Spitze stehend"></div>
  <blockquote class="quote abs">
    <span class="soft i1">„Tanz ist</span>
    <span class="soft i2">Nahrung</span>
    <span class="strong i3">für Gehirn</span>
    <span class="strong i4">und Seele“</span>
  </blockquote>

  <div class="copy abs">
    <p><span class="lead-title">Im Tanz bilden Körper und Geist eine Einheit.</span><br>
    <span class="lead">Neue Bereiche im Gehirn werden erschlossen und immer wieder trainiert und gestärkt.</span></p>
    <p class="benefit-intro">Eine Grundausbildung im Klassischen Ballett führt zu:</p>
    <ul class="benefit-list">
      <li>einer gesunden Kräftigung der gesamten Muskulatur</li>
      <li>einer Förderung einer guten Körperhaltung</li>
      <li>einer erweiterten Wahrnehmungsfähigkeit</li>
      <li>einer Verbesserung des Konzentrationsvermögen</li>
      <li>einem verstärktem Selbstwertgefühl</li>
      <li>Disziplin, Respekt und Genauigkeit</li>
    </ul>
    <p><span class="bold">Besonders für Kinder unterstützt Ballettunterricht jegliche Bewegungsform und verhilft nachweislich zu </span><span class="accent">besseren Schulergebnissen.</span></p>
    <p class="accent">Tanzen, Kunst und Musik fördern in Ihrer Einheit die emotionale Ausgeglichenheit und den Sinn für Grazie und Harmonie.</p>
  </div>

  <div class="gallery-photo gallery-photo--show abs" role="img" aria-label="Foto: Kinder in rosa Tutus bei einer Aufführung im Freien"></div>
  <div class="gallery-photo gallery-photo--class abs" role="img" aria-label="Foto: Kinder in Marienkäfer-Kostümen im Ballettsaal"></div>

  <div class="membership abs">Mitglied im Tanzpädagogik-Verbund Nord</div>
</section>

</body>
</html>
```